Toronto's Airline, based in Downtown looking for a whole new look and feel.

SoarVex is looking for a new look in our website. We are an airline based at Marlow Quay Airfield in Toronto. You can view our current website/services at www.soarvex-example.com. We are expanding our services and look forward to a very sleek and modernized website. Please view the different pages on our website, we also need to add several new plane types as we have expanded and the website is not current. Would also be interesting to have a news feed or update feed through a widget which would be easy to use and update. we will also be implementing 2 third party programs called bookplume and skyledgra on the website, both are tour based and airline based sales and management functions.

Target Market(s)

Commuters, travel, tourism, dates, general public

Industry/Entity Type

Airline

Coding

Coded - Design and coding required

Number of Pages Required

5+ page

Font styles to use
Other font styles liked:
• Toronto subway font would be nice

Requirements
Must have
• A modern feel, easy to use, our booking function is currently a bit confusing which we will be working on. Content can be taken from our current website www.soarvex-example.com
Nice to have
• work with out theme colours of blue and light grey

```html
<!DOCTYPE html>
<html lang="en">
<head>
<meta charset="utf-8">
<title>SoarVex – Toronto's Airline</title>
<link href="https://fonts.googleapis.com/css2?family=Montserrat:wght@600;700&family=Raleway:wght@400;500;600&family=Open+Sans:wght@400;600&display=swap" rel="stylesheet">
<style>
:root{
  --blue:#3a6ab5;
  --blue-dark:#2c579c;
  --grey-nav:#8a8b8d;
  --grey-band:#8d8e90;
  --ink:#333;
  --muted:#777;
  --line:#e4e4e4;
  --white:#fff;
  --night:#1f2630;
}
*{box-sizing:border-box;margin:0;padding:0}
html,body{width:1200px;height:2830px;overflow:hidden;background:var(--white)}
body{position:relative;font-family:"Open Sans",Arial,sans-serif;color:var(--ink)}
.abs{position:absolute}
.heading{font-family:"Raleway",Arial,sans-serif;font-weight:500;text-transform:uppercase;color:var(--ink)}

/* header */
.brand{left:132px;top:28px;display:flex;align-items:center;gap:12px}
.brand-mark{width:44px;height:44px;border-radius:50%;background:var(--blue)}
.brand-name{font-family:"Raleway",Arial,sans-serif;font-weight:600;font-size:34px;color:var(--blue);letter-spacing:1px}
.search{left:705px;top:42px;width:240px;height:22px;border-bottom:1px solid #ccc;font-size:11px;color:#888}
.search svg{position:absolute;right:0;top:0}
.btn{display:inline-flex;align-items:center;justify-content:center;background:var(--blue);color:var(--white);border-radius:22px;font-size:12px;font-family:"Open Sans",Arial,sans-serif;text-transform:uppercase;letter-spacing:.3px}
.book-now{left:963px;top:32px;width:104px;height:38px}

.nav{left:0;top:105px;width:1200px;height:52px;background:var(--grey-nav)}
.nav ul{list-style:none;display:flex;position:absolute;left:132px;width:936px;height:52px}
.nav li{flex:1;display:flex;align-items:center;justify-content:center;color:var(--white);font-size:12px;text-transform:uppercase;border-right:1px solid rgba(255,255,255,.15)}
.nav li:last-child{border-right:0}
.nav li.active{background:var(--blue)}

/* hero */
.hero{left:0;top:157px;width:1200px;height:526px;background:linear-gradient(180deg,#9db7d3 0%,#6d8fb0 35%,#3f5c78 70%,#2a3d52 100%)}
.hero-title{right:132px;top:300px;text-align:right;font-family:"Montserrat",Arial,sans-serif;font-weight:700;font-size:56px;line-height:70px;color:var(--white);text-transform:uppercase}
.hero-btn{left:893px;top:458px;width:175px;height:38px;font-size:11px}
.dots{left:560px;top:618px;display:flex;gap:22px}
.dots span{width:12px;height:12px;border-radius:50%;border:1.5px solid var(--white)}
.dots span.on{background:var(--white)}

/* welcome */
.section-icon{left:576px}
.welcome-title{left:0;width:1200px;text-align:center;font-size:27px}
.welcome-intro{left:200px;top:805px;width:800px;text-align:center;font-size:9px;line-height:19px;text-transform:uppercase;color:var(--muted);letter-spacing:.3px}
.card{top:870px;width:295px;height:320px;border:1px solid var(--line);box-shadow:0 0 4px rgba(0,0,0,.06);background:var(--white);text-align:center}
.card-photo{position:absolute;left:8px;top:8px;width:277px;height:163px}
.card-icon{position:absolute;left:116px;top:138px;width:64px;height:64px;border-radius:50%;background:var(--blue);border:3px solid var(--white);display:flex;align-items:center;justify-content:center}
.card-title{position:absolute;top:212px;width:100%;font-family:"Raleway",Arial,sans-serif;font-size:14px;text-transform:uppercase}
.card-text{position:absolute;top:238px;left:25px;width:245px;font-size:10.5px;line-height:23px;color:var(--muted)}
.cta{left:505px;top:1222px;width:190px;height:38px;font-size:11px}

/* shuttle band */
.band{left:0;top:1319px;width:1200px;height:494px;background:linear-gradient(180deg,#3a4450 0%,#252d38 60%,#1b222c 100%)}
.band-title{color:var(--white)}
.shuttle-heading{left:132px;top:1505px;font-family:"Raleway",Arial,sans-serif;font-size:16px;color:var(--white)}
.shuttle-copy{left:132px;width:440px;font-size:10.5px;line-height:24px;color:#d6d9dd}
.video{left:630px;top:1487px;width:438px;height:263px;border:3px solid var(--white);background:var(--white)}
.video-frame{position:absolute;left:0;top:0;width:432px;height:232px;background:linear-gradient(135deg,#8ea3b8 0%,#c9d2db 40%,#5d6b7a 100%)}
.video-play{position:absolute;left:190px;top:90px;width:52px;height:52px;border-radius:50%;background:rgba(0,0,0,.45);border:2px solid rgba(255,255,255,.8)}
.video-bar{position:absolute;left:0;top:232px;width:432px;height:25px;display:flex;align-items:center;gap:8px;padding:0 10px;font-size:7px;color:#555}
.track{height:3px;background:#ddd;position:relative;flex:1}
.track i{position:absolute;left:0;top:0;height:3px;background:#d9534f}

/* news */
.news-title{left:132px;top:1870px;font-size:19px}
.news-item{left:132px;width:600px;height:120px}
.news-thumb{position:absolute;left:0;top:0;width:138px;height:104px;border:1px solid var(--line);padding:5px}
.news-thumb div{width:100%;height:100%}
.news-head{position:absolute;left:168px;top:2px;font-size:11px;color:var(--blue)}
.news-text{position:absolute;left:168px;top:28px;width:420px;font-size:10px;line-height:21px;color:var(--muted)}
.news-date{position:absolute;left:168px;top:80px;display:flex;align-items:center;gap:10px;font-size:10px;color:var(--blue);text-transform:uppercase}
.date-icon{width:30px;height:30px;border-radius:50%;border:1px solid var(--line);display:flex;align-items:center;justify-content:center}

.support{left:783px;top:1875px;width:285px;height:307px;border:1px solid var(--line)}
.support-head{height:58px;background:var(--blue);color:var(--white);display:flex;align-items:center;justify-content:center;font-family:"Raleway",Arial,sans-serif;font-size:19px;text-transform:uppercase}
.partner{position:absolute;left:22px;width:239px;height:92px;border:1px solid var(--line);display:flex;align-items:center;justify-content:center;font-family:"Raleway",Arial,sans-serif;font-size:26px;color:#2a3f66;letter-spacing:1px}

/* gallery */
.gallery{left:0;top:2238px;width:1200px;height:382px;background:var(--grey-band)}
.gallery-title{color:var(--white)}
.gallery-row{left:132px;top:2385px;width:936px;height:182px;display:flex;gap:2px}
.gallery-row div{flex:1}
.arrow{top:2458px;width:38px;height:38px;border-radius:50%;background:rgba(255,255,255,.55);display:flex;align-items:center;justify-content:center}

/* footer */
.footer-brand{left:132px;top:2672px}
.col-title{font-family:"Raleway",Arial,sans-serif;font-size:13px;text-transform:uppercase;font-weight:500}
.contact-line{display:flex;align-items:flex-start;gap:8px;font-size:11px;line-height:22px;color:#555}
.divider-v{width:1px;background:var(--line)}
.email-field{left:652px;top:2692px;width:205px;height:36px;border:1px solid var(--line);font-size:11px;color:#888;padding:10px 12px}
.subscribe{left:855px;top:2692px;width:95px;height:36px;font-size:10px;font-weight:600}
.social{width:36px;height:36px;border-radius:50%;border:1px solid #999}
.footer-rule{left:132px;top:2773px;width:936px;height:1px;background:var(--line)}
.copyright{left:0;top:2788px;width:1200px;text-align:center;font-size:11px;color:#777}
</style>
</head>
<body>

<!-- header -->
<div class="abs brand"><span class="brand-mark"></span><span class="brand-name">SoarVex</span></div>
<div class="abs search">Search
  <svg width="16" height="16" viewBox="0 0 16 16"><circle cx="6.5" cy="6.5" r="5" fill="none" stroke="#999" stroke-width="1.5"/><line x1="10" y1="10" x2="15" y2="15" stroke="#999" stroke-width="1.5"/></svg>
</div>
<a class="abs btn book-now">Book Now</a>

<nav class="abs nav">
  <ul>
    <li class="active">Home</li><li>Flights</li><li>Charter &amp; Fleet</li><li>Packages</li><li>Gallery</li><li>Contact</li><li>FAQ</li>
  </ul>
</nav>

<!-- hero -->
<div class="abs hero" role="img" aria-label="White private jet flying above downtown Toronto"></div>
<h1 class="abs hero-title">Airline<br>Adventure</h1>
<a class="abs btn hero-btn">View More Information</a>
<div class="abs dots"><span></span><span class="on"></span><span></span></div>

<!-- welcome -->
<svg class="abs section-icon" style="top:728px" width="48" height="36" viewBox="0 0 48 36"><path d="M4 26 L44 8 L46 12 L28 22 L30 32 L26 33 L20 24 L10 28 Z" fill="var(--blue)"/></svg>
<h2 class="abs heading welcome-title" style="top:762px">Welcome to SoarVex</h2>
<p class="abs welcome-intro">Looking for something new and exciting in Toronto? SoarVex, a private airline based at Marlow Quay Airfield in downtown Toronto. SoarVex offers adventure/scenic flights in intimate private airplanes...</p>

<article class="abs card" style="left:132px">
  <div class="card-photo" role="img" aria-label="Passenger jet above clouds in blue sky" style="background:linear-gradient(180deg,#0d3a7a,#4f86c6 60%,#cfe0f2)"></div>
  <div class="card-icon"><svg width="28" height="28" viewBox="0 0 24 24"><path d="M21 16v-2l-8-5V3.5a1.5 1.5 0 0 0-3 0V9l-8 5v2l8-2.5V19l-2 1.5V22l3.5-1 3.5 1v-1.5L13 19v-5.5z" fill="#fff"/></svg></div>
  <h3 class="card-title">Flights</h3>
  <p class="card-text">Consequuntur magni dolores eos qui voluptatem sequi nesciunt. Neque porro quisquam dolorem ipsum quia dolor sit amet...</p>
</article>
<article class="abs card" style="left:452px">
  <div class="card-photo" role="img" aria-label="Private turboprop aircraft parked in a hangar" style="background:linear-gradient(180deg,#8a8176,#c9c1b4 50%,#6e665c)"></div>
  <div class="card-icon"><svg width="26" height="26" viewBox="0 0 24 24" fill="#fff"><path d="M12 2 2 7v2h20V7z"/><rect x="4" y="10" width="3" height="8"/><rect x="10.5" y="10" width="3" height="8"/><rect x="17" y="10" width="3" height="8"/><rect x="2" y="19" width="20" height="3"/></svg></div>
  <h3 class="card-title">Private Charter</h3>
  <p class="card-text">Consequuntur magni dolores eos qui voluptatem sequi nesciunt. Neque porro quisquam dolorem ipsum quia dolor sit amet...</p>
</article>
<article class="abs card" style="left:773px">
  <div class="card-photo" role="img" aria-label="Traveller at airport window at sunset" style="background:linear-gradient(120deg,#2b2a2a,#7a6048 50%,#e8c79a 75%,#3a3430)"></div>
  <div class="card-icon"><svg width="24" height="24" viewBox="0 0 24 24"><path d="M3 17.5V21h3.5L18 9.5 14.5 6zM20.7 6.8a1 1 0 0 0 0-1.4l-2.1-2.1a1 1 0 0 0-1.4 0l-1.6 1.6 3.5 3.5z" fill="#fff"/></svg></div>
  <h3 class="card-title">Contact</h3>
  <p class="card-text">Consequuntur magni dolores eos qui voluptatem sequi nesciunt. Neque porro quisquam dolorem ipsum quia dolor sit amet...</p>
</article>
<a class="abs btn cta">Click Here to Book Now!</a>

<!-- shuttle band -->
<div class="abs band" role="img" aria-label="Toronto skyline at dusk seen from above"></div>
<svg class="abs section-icon" style="top:1385px" width="48" height="36" viewBox="0 0 48 36"><path d="M4 26 L44 8 L46 12 L28 22 L30 32 L26 33 L20 24 L10 28 Z" fill="#fff"/></svg>
<h2 class="abs heading welcome-title band-title" style="top:1418px">Welcome to SoarVex</h2>
<h3 class="abs shuttle-heading">SoarVex Toronto - Niagara Shuttle</h3>
<p class="abs shuttle-copy" style="top:1542px">Exercitationem ullam corporis suscipit laboriosam, nisi ut aliquid ex ea consequatur? Quis autem vel eum iure reprehenderit qui in ea voluptate qui in ea voluptate velit esse quam nihil molestiae consequatur, vel illum qui dolorem physical exercise, except to obtain some advantage from it? But who has any right...</p>
<p class="abs shuttle-copy" style="top:1654px">Autem vel eum iure reprehenderit qui in ea voluptate qui in ea voluptate velit esse quam nihil molestiae consequatur, vel illum qui dolorem physical exercise, except to obtain some advantage from it? But who has any right...</p>

<div class="abs video">
  <div class="video-frame" role="img" aria-label="Pilot greeting a passenger beside a small aircraft"></div>
  <div class="video-play"><svg width="48" height="48" viewBox="0 0 48 48"><path d="M19 15 L33 24 L19 33 Z" fill="#fff"/></svg></div>
  <div class="video-bar">
    <svg width="8" height="8" viewBox="0 0 8 8"><path d="M1 0 L7 4 L1 8Z" fill="#444"/></svg>
    <span>00:00/00:00</span>
    <div class="track"><i style="width:80%"></i></div>
    <svg width="10" height="8" viewBox="0 0 10 8"><path d="M0 2.5h2.5L5.5 0v8L2.5 5.5H0z" fill="#444"/></svg>
    <div class="track" style="flex:0 0 40px"><i style="width:100%"></i></div>
  </div>
</div>

<!-- news -->
<h2 class="abs heading news-title">Recent News</h2>
<article class="abs news-item" style="top:1922px">
  <div class="news-thumb"><div role="img" aria-label="Small aircraft on the tarmac with city skyline behind" style="background:linear-gradient(180deg,#a9c4de,#7f8f9c 60%,#59606a)"></div></div>
  <h4 class="news-head">Sed quia non numquam eius modi tempora incidunt ut labore...</h4>
  <p class="news-text">Except to obtain some advantage from it? But who has any right to find fault with a man who chooses to enjoy a pleasure consequences...</p>
  <div class="news-date"><span class="date-icon"><svg width="12" height="12" viewBox="0 0 12 12"><rect x="1" y="2" width="10" height="9" fill="none" stroke="var(--blue)"/><rect x="1" y="2" width="10" height="3" fill="var(--blue)"/></svg></span>Posted on 24 March, 2017</div>
</article>
<article class="abs news-item" style="top:2072px">
  <div class="news-thumb"><div role="img" aria-label="Downtown Toronto towers under blue sky" style="background:linear-gradient(180deg,#b8cde0,#6f7c88 55%,#3f4752)"></div></div>
  <h4 class="news-head">Sed quia non numquam eius modi tempora incidunt ut labore...</h4>
  <p class="news-text">Except to obtain some advantage from it? But who has any right to find fault with a man who chooses to enjoy a pleasure consequences...</p>
  <div class="news-date"><span class="date-icon"><svg width="12" height="12" viewBox="0 0 12 12"><rect x="1" y="2" width="10" height="9" fill="none" stroke="var(--blue)"/><rect x="1" y="2" width="10" height="3" fill="var(--blue)"/></svg></span>Posted on 24 March, 2017</div>
</article>

<aside class="abs support">
  <div class="support-head">Our Support</div>
  <div class="partner" style="top:82px">skyledgra</div>
  <div class="partner" style="top:187px">bookplume</div>
</aside>

<!-- gallery -->
<div class="abs gallery"></div>
<svg class="abs section-icon" style="top:2290px" width="48" height="36" viewBox="0 0 48 36"><path d="M4 26 L44 8 L46 12 L28 22 L30 32 L26 33 L20 24 L10 28 Z" fill="#fff"/></svg>
<h2 class="abs heading welcome-title gallery-title" style="top:2322px">Our Gallery</h2>
<div class="abs gallery-row">
  <div role="img" aria-label="Aircraft wing over a hazy coastline" style="background:linear-gradient(160deg,#6e5a48,#b9a68c 50%,#4e5a58)"></div>
  <div role="img" aria-label="Aerial view of green countryside and a lake" style="background:linear-gradient(160deg,#7d8a70,#5c6c52 50%,#8aa3a8)"></div>
  <div role="img" aria-label="Aerial view straight down onto city towers" style="background:linear-gradient(160deg,#3a352f,#6e5e4c 50%,#2b2824)"></div>
  <div role="img" aria-label="City skyline on a turquoise lakefront" style="background:linear-gradient(180deg,#a6bdd4,#c79a6a 50%,#2f8a94)"></div>
</div>
<div class="abs arrow" style="left:103px"><svg width="14" height="14" viewBox="0 0 14 14"><path d="M13 7H2M6 2 1 7l5 5" fill="none" stroke="#555" stroke-width="2"/></svg></div>
<div class="abs arrow" style="left:1059px"><svg width="14" height="14" viewBox="0 0 14 14"><path d="M1 7h11M8 2l5 5-5 5" fill="none" stroke="#555" stroke-width="2"/></svg></div>

<!-- footer -->
<div class="abs brand footer-brand"><span class="brand-mark"></span><span class="brand-name">SoarVex</span></div>
<h5 class="abs col-title" style="left:348px;top:2660px">Contact Us</h5>
<div class="abs contact-line" style="left:348px;top:2684px;width:130px">
  <svg width="10" height="14" viewBox="0 0 10 14" style="margin-top:4px"><path d="M5 0a5 5 0 0 0-5 5c0 4 5 9 5 9s5-5 5-9a5 5 0 0 0-5-5zm0 7a2 2 0 1 1 0-4 2 2 0 0 1 0 4z" fill="var(--blue)"/></svg>
  <span>Marlow Quay Airfield...</span>
</div>
<div class="abs contact-line" style="left:510px;top:2684px">
  <svg width="12" height="12" viewBox="0 0 24 24" style="margin-top:5px"><path d="M6.6 10.8a15 15 0 0 0 6.6 6.6l2.2-2.2a1 1 0 0 1 1-.25 11.4 11.4 0 0 0 3.6.57 1 1 0 0 1 1 1V20a1 1 0 0 1-1 1A17 17 0 0 1 3 4a1 1 0 0 1 1-1h3.5a1 1 0 0 1 1 1c0 1.25.2 2.45.57 3.6a1 1 0 0 1-.25 1z" fill="var(--blue)"/></svg>
  <span>1-800-555-0142</span>
</div>
<div class="abs contact-line" style="left:510px;top:2710px">
  <svg width="12" height="10" viewBox="0 0 12 10" style="margin-top:6px"><rect width="12" height="10" rx="1" fill="var(--blue)"/><path d="M0 1l6 4 6-4" fill="none" stroke="#fff"/></svg>
  <span>info@soarvex-example.com</span>
</div>
<div class="abs divider-v" style="left:632px;top:2655px;height:95px"></div>
<h5 class="abs col-title" style="left:652px;top:2660px">Newsletter</h5>
<div class="abs email-field">Email:</div>
<a class="abs btn subscribe">Subscribe</a>
<div class="abs divider-v" style="left:967px;top:2655px;height:95px"></div>
<h5 class="abs col-title" style="left:988px;top:2660px">Follow Us</h5>
<span class="abs social" style="left:988px;top:2692px"></span>
<span class="abs social" style="left:1030px;top:2692px"></span>
<div class="abs footer-rule"></div>
<p class="abs copyright">Copyright © 2017 soarvex-example.com all rights are reserved</p>

</body>
</html>
```